Criação de Folder para Tecnologia & Ciencias
A empresa queria:
" A Quitafor é uma empresa que desenvolve e fornece o sistema de cobrança Quitafor para empresas de cobrança (escritórios de cobrança, assessorias de cobranças, escritórios de advogados), tais clientes chamamos de ASSESSORIAS, e também fornecemos o sistema para empresas que possuem uma grande quantidade de clientes inadimplentes e que fazem a cobrança destes clientes internamente através de um departamento de cobrança, estes clientes chamamos de CREDORES. Alguns clientes ASSESSORIAS: www.grupoltv.com.br www.dornelesmota.com.br www.rixamonte.com.br Alguns clientes CREDORES: www.brightlane.com www.grupovelarim.com.br www.tadeus.com.br Todos os produtos e serviços que comercializamos são através da plataforma Quitafor, por exemplo, para que um cliente utilize nosso produto “Painel de Acordos” ele precisa contratar o Quitafor já que suas configurações são através do sistema, da mesma forma o serviço de “SMS”, já que as campanhas são criadas e disparadas pelo sistema Quitafor. O sistema Quitafor “nasceu” primeiro que a empresa Quitafor, já que dois dos atuais sócios possuíram uma empresa anterior de 2012 até a abertura da Quitafor em 1 de setembro de 2015. Esta empresa desenvolvia um sistema focado para assessorias de cobrança, porém em uma tecnologia antiga, e então resolveram criar um novo software com tecnologias atuais na época e para isto buscaram um investidor e juntos optaram por criar uma nova empresa, uma nova marca. Nossa logo foi construída através da plataforma Marca Pronta e gostamos muito do resultado! E estamos aqui novamente buscando que seus profissionais nos ajudem a criar novos materiais que hoje se fazem necessários para nós. "

```html
<!DOCTYPE html>
<html lang="pt-BR">
<head>
<meta charset="utf-8">
<title>Folder Quitafor</title>
<link rel="stylesheet" href="https://fonts.googleapis.com/css2?family=Montserrat:wght@400;600;700;800&display=swap">
<style>
  :root{
    --blue:#1d3f8f;
    --blue-dark:#142d69;
    --orange:#f28c1b;
    --sky:#e3f1fa;
    --sky-2:#c9e4f4;
    --ink:#3b4250;
    --paper:#ffffff;
    --backdrop:#efece6;
  }
  *{box-sizing:border-box;margin:0;padding:0}
  html,body{width:1200px;height:1200px;overflow:hidden}
  body{background:var(--backdrop);font-family:"Montserrat",Arial,sans-serif;color:var(--ink)}
  .folder{position:absolute;left:30px;top:290px;width:1140px;height:620px;background:var(--paper);
    display:flex;box-shadow:0 6px 22px rgba(0,0,0,.12)}
  .panel{width:380px;height:100%;position:relative;padding:28px 26px;display:flex;flex-direction:column;gap:12px}
  .panel + .panel{border-left:1px solid #e6e9ef}
  .tag{align-self:center;padding:6px 20px;border-radius:14px;color:#fff;font-weight:700;font-size:13px;font-style:normal}
  .tag--blue{background:var(--blue)}
  .tag--orange{background:var(--orange)}
  .tag--left{align-self:flex-start}
  .copy{font-size:9.5px;line-height:1.55;text-align:justify}
  .subhead{font-size:11px;font-weight:700;color:var(--blue)}
  .clients{display:grid;grid-template-columns:repeat(3,1fr);gap:10px 14px;padding:4px 6px}
  .badge{height:26px;border-radius:4px;background:#d7dde8}
  .band{margin:auto -26px 0;background:var(--sky);padding:14px 26px;display:flex;gap:14px;align-items:center}
  .band__art{width:150px;height:80px;border-radius:6px;background:linear-gradient(135deg,var(--sky-2),#9fc4e3)}
  .band__text{font-size:13px;font-weight:700;color:var(--blue);line-height:1.3}
  .strip{margin:0 -26px;background:var(--blue);color:#fff;font-size:9.5px;font-weight:600;padding:6px 26px}
  .brand{display:flex;align-items:center;gap:8px;margin:0 -26px -28px;padding:10px 26px 16px;background:var(--sky)}
  .brand__dot{width:14px;height:14px;border-radius:50%;background:var(--blue)}
  .brand__name{font-size:24px;font-weight:800;color:var(--blue)}
  .brand__line{font-size:9px;color:var(--blue);margin-left:auto}
  .flow{width:100%;height:190px}
  .modules{display:flex;gap:16px}
  .module{flex:1}
  .module__title{font-size:12px;font-weight:800;color:var(--blue);text-align:center;margin-bottom:4px}
  .extras{display:grid;grid-template-columns:1fr 1fr;gap:4px 14px;font-size:9.5px}
  .extras li{list-style:none;padding-left:12px;position:relative}
  .extras li::before{content:"";position:absolute;left:0;top:4px;width:6px;height:6px;background:var(--orange);border-radius:50%}
  .site{margin:auto -26px -28px;background:var(--blue);color:#fff;padding:12px 26px;font-size:12px;text-align:right}
  .site strong{font-size:14px;font-weight:800}
</style>
</head>
<body>
<main class="folder">
  <section class="panel panel--intro">
    <span class="tag tag--blue">Conheça a Quitafor</span>
    <p class="copy">A Quitafor desenvolve e fornece um sistema completo de cobrança para assessorias, escritórios de advocacia e credores que realizam a cobrança de seus clientes internamente.</p>
    <p class="copy">Nosso sistema nasceu da experiência de sócios que atuam no mercado desde 2012, unindo tecnologia atual e conhecimento prático do dia a dia da cobrança.</p>
    <h3 class="subhead">Alguns de nossos clientes</h3>
    <div class="clients">
      <div class="badge"></div><div class="badge"></div><div class="badge"></div>
      <div class="badge"></div><div class="badge"></div><div class="badge"></div>
    </div>
    <div class="band">
      <div class="band__art" role="img" aria-label="Ilustração de equipe usando o sistema de cobrança"></div>
      <p class="band__text">Soluções inteligentes para a sua recuperação de crédito</p>
    </div>
    <p class="strip">Sistema de cobrança para assessorias e credores</p>
    <div class="brand">
      <span class="brand__dot"></span>
      <span class="brand__name">Quitafor</span>
      <span class="brand__line">Tecnologia em cobrança desde 2015</span>
    </div>
  </section>

  <section class="panel panel--flow">
    <span class="tag tag--blue">Como funciona o sistema?</span>
    <svg class="flow" viewBox="0 0 330 190" font-family="Montserrat, Arial, sans-serif" font-size="8" fill="none">
      <defs><marker id="arrow" markerWidth="6" markerHeight="6" refX="5" refY="3" orient="auto"><path d="M0,0 L6,3 L0,6 z" fill="#1d3f8f"/></marker></defs>
      <g stroke="#1d3f8f" stroke-width="1.2">
        <rect x="4" y="20" width="56" height="22" rx="3"/>
        <rect x="4" y="84" width="56" height="22" rx="3"/>
        <rect x="4" y="148" width="56" height="22" rx="3"/>
        <rect x="90" y="20" width="60" height="22" rx="3"/>
        <rect x="90" y="60" width="60" height="22" rx="3"/>
        <rect x="90" y="100" width="60" height="22" rx="3"/>
        <rect x="90" y="140" width="60" height="22" rx="3"/>
        <rect x="180" y="40" width="60" height="22" rx="3"/>
        <rect x="180" y="90" width="60" height="22" rx="3"/>
        <rect x="180" y="140" width="60" height="22" rx="3"/>
        <path d="M60 31 H88 M60 95 H75 V71 H88 M60 95 H75 V111 H88 M60 159 H88" marker-end="url(#arrow)"/>
        <path d="M150 31 H165 V51 H178 M150 111 H178 M150 151 H178" marker-end="url(#arrow)"/>
        <path d="M240 51 H264 M240 101 H264 M240 151 H264" marker-end="url(#arrow)"/>
      </g>
      <rect x="266" y="10" width="60" height="170" rx="4" fill="#f28c1b"/>
      <g fill="#1d3f8f" text-anchor="middle">
        <text x="32" y="34">Carteira</text><text x="32" y="98">Importação</text><text x="32" y="162">Credor</text>
        <text x="120" y="34">Acionamento</text><text x="120" y="74">Negociação</text><text x="120" y="114">Acordo</text><text x="120" y="154">Boleto</text>
        <text x="210" y="54">Cobrança</text><text x="210" y="104">Pagamento</text><text x="210" y="154">Baixa</text>
      </g>
      <g fill="#fff" text-anchor="middle" font-weight="700">
        <text x="296" y="50">Painel de</text><text x="296" y="60">Acordos</text>
        <text x="296" y="95">SMS</text><text x="296" y="130">E-mail</text><text x="296" y="165">URA</text>
      </g>
    </svg>
    <span class="tag tag--orange">Diferenciais Quitafor</span>
    <p class="copy">Plataforma web segura, com acesso de qualquer lugar, controle completo das carteiras, indicadores em tempo real e automação das rotinas de negociação, acordos e emissão de boletos.</p>
    <span class="tag tag--blue tag--left">Integrações</span>
    <p class="copy">Conecte o Quitafor aos seus parceiros, bancos e ferramentas de comunicação para agilizar toda a operação de cobrança.</p>
  </section>

  <section class="panel panel--modules">
    <span class="tag tag--blue tag--left">Nossa plataforma</span>
    <p class="copy">Todos os produtos e serviços que oferecemos funcionam dentro da plataforma Quitafor, com configuração simples e campanhas criadas e disparadas pelo próprio sistema.</p>
    <span class="tag tag--blue tag--left">Segurança</span>
    <p class="copy">Dados protegidos, acessos controlados por perfil e histórico completo de cada ação realizada.</p>
    <span class="tag tag--orange">Módulo de Cobrança</span>
    <div class="modules">
      <div class="module"><h4 class="module__title">Módulo Assessoria</h4><p class="copy">Gestão de várias carteiras, credores e equipes em um só lugar.</p></div>
      <div class="module"><h4 class="module__title">Módulo Credor</h4><p class="copy">Cobrança interna dos seus clientes com total controle e agilidade.</p></div>
    </div>
    <span class="tag tag--orange">Produtos Adicionais</span>
    <h4 class="subhead">Conheça também:</h4>
    <ul class="extras">
      <li>Painel de Acordos</li><li>Campanhas de SMS</li>
      <li>Discador</li><li>Higienização</li>
      <li>Relatórios</li><li>Cobrança digital</li>
    </ul>
    <p class="site">Acesse nosso site: <strong>www.quitafor.com.br</strong></p>
  </section>
</main>
</body>
</html>
```